Business Card Design for Boutique Agriculture Consulting Practice

Develop a modern Business card design using uploaded logos . Using the color specs 6C344F rgb(108, 52, 79) The fonts are trajan pro and eurostile. The business owner is a woman and should have a hint of femininity. This is what is behind the naming of the company: Rock roads are synonymous with the rural US landscape, where the corn grows and the cattle graze or for Tall Meadow Advisory home. But don’t let the dust get in your eyes, rock roads have edge and are often the only path to a spectacular destination. To navigate them one must know where they are going, have the courage to take a new path and the willingness to adjust their plans to get there.
Target Market(s)
Marketing Professionals
Industry/Entity Type
Agriculture
Contact Information for Business Card
Lorinda Bastable
Title: Founder and CEO
Address: 20487 Whitlow Lane, Olathe Kansas 66062
Email: lb@tallmeadowadvisory.example
Phone: 317.555.0148
Website: www.tallmeadowadvisory.example
Font styles to use
Other font styles liked:
- trajan pro and eurostile
Requirements
Must have
- Please use the correct color specs. Logo color specs are 6C344F rgb(108, 52, 79) The fonts are trajan pro and eurostile. Name, email and phone be the most important information included on the card
Should not have
- additional graphics

```html
<!DOCTYPE html>
<html lang="en">
<head>
<meta charset="utf-8">
<title>Tall Meadow Advisory – Business Card</title>
<link rel="stylesheet" href="https://fonts.googleapis.com/css2?family=Cinzel:wght@600&family=Open+Sans:wght@400;700&display=swap">
<style>
  :root {
    --plum: #6c344f;
    --paper: #ffffff;
    --ink: #3a3a3a;
    --backdrop: #e9e4df;
  }
  html, body {
    margin: 0;
    padding: 0;
    width: 1200px;
    height: 1145px;
    overflow: hidden;
    background: var(--backdrop);
  }
  .canvas {
    position: relative;
    width: 1200px;
    height: 1145px;
  }
  .card {
    position: absolute;
    top: 427px;
    width: 502px;
    height: 297px;
    box-shadow: 0 4px 14px rgba(0, 0, 0, 0.18);
    overflow: hidden;
  }
  .card--front { left: 89px; background: var(--paper); }
  .card--back { left: 611px; background: var(--plum); }

  .wordmark {
    position: absolute;
    margin: 0;
    font-family: "Cinzel", serif;
    font-weight: 600;
    font-size: 27px;
    line-height: 1.05;
    text-align: center;
    letter-spacing: 0.5px;
  }
  .card--front .wordmark { left: 24px; top: 60px; width: 220px; color: var(--plum); }
  .card--back .wordmark { left: 258px; top: 120px; width: 232px; color: var(--paper); }

  .contact {
    position: absolute;
    left: 25px;
    top: 160px;
    font-family: "Open Sans", sans-serif;
    color: var(--ink);
  }
  .contact__name {
    margin: 0;
    font-weight: 700;
    font-size: 14px;
    letter-spacing: 0.3px;
    color: var(--plum);
    text-transform: uppercase;
  }
  .contact__title {
    margin: 0 0 16px;
    font-size: 12px;
  }
  .contact__list {
    list-style: none;
    margin: 0;
    padding: 0;
    font-size: 12.5px;
    line-height: 17px;
  }
  .contact__list li { display: flex; align-items: center; gap: 4px; }
  .contact__list svg { width: 11px; height: 11px; fill: var(--ink); flex: none; }
  .contact__address { margin-top: 3px; padding-left: 0; }
</style>
</head>
<body>
<main class="canvas">
  <section class="card card--front" aria-label="Card front">
    <p class="wordmark">Tall Meadow<br>Advisory</p>
    <div class="contact">
      <h1 class="contact__name">Lorinda Bastable</h1>
      <p class="contact__title">Founder and CEO</p>
      <ul class="contact__list">
        <li>
          <svg viewBox="0 0 12 12" aria-hidden="true"><path d="M1 4c0-1.5 2-2.5 5-2.5S11 2.5 11 4v1H8.5V3.8h-5V5H1z M3 6h6l1.5 4.5h-9z"/></svg>
          317.555.0148
        </li>
        <li>
          <svg viewBox="0 0 12 12" aria-hidden="true"><path d="M1 2.5h10v7H1z" /><path d="M1.5 3l4.5 3.5L10.5 3" fill="none" stroke="#fff" stroke-width="1"/></svg>
          lb@tallmeadowadvisory.example
        </li>
        <li>
          <svg viewBox="0 0 12 12" aria-hidden="true"><circle cx="6" cy="6" r="5"/><path d="M1 6h10M6 1c-2 2.5-2 7.5 0 10M6 1c2 2.5 2 7.5 0 10" fill="none" stroke="#fff" stroke-width="0.8"/></svg>
          www.tallmeadowadvisory.example
        </li>
        <li class="contact__address">20487 Whitlow Lane, Olathe Kansas 66062</li>
      </ul>
    </div>
  </section>

  <section class="card card--back" aria-label="Card back">
    <p class="wordmark">Tall Meadow<br>Advisory</p>
  </section>
</main>
</body>
</html>
```